Cybersecurity company is looking for business card.

I need a business card design for our company, we are a cybersecurity company providing advance technology to protect agains any kind of malware. We need a fresh modern design it should communicate modern, technology and growth.

Target Market(s)

Business to business

Industry/Entity Type

Business

Contact Information for Business Card

Should have location, address, fax, mobile, phone, email and website.

Requirements
Must have
• Must follow company's logo color and style. Must have the company's log on its.

```html
<!DOCTYPE html>
<html lang="en">
<head>
<meta charset="utf-8">
<title>Vextral Business Card</title>
<link href="https://fonts.googleapis.com/css2?family=Lato:wght@400;700;900&display=swap" rel="stylesheet">
<style>
  :root {
    --ink: #0a0a0a;
    --paper: #ffffff;
    --accent: #b01e23;
    --stage: #e4e4e4;
  }
  * { margin: 0; padding: 0; box-sizing: border-box; }
  html, body { width: 1200px; height: 926px; overflow: hidden; }
  body {
    background: var(--stage);
    font-family: "Lato", Arial, sans-serif;
    display: flex;
    flex-direction: column;
    align-items: center;
    justify-content: center;
    gap: 40px;
  }
  .card {
    position: relative;
    width: 700px;
    height: 400px;
    background: var(--ink);
    overflow: hidden;
    box-shadow: 0 6px 18px rgba(0,0,0,0.18);
  }
  /* back side */
  .card-back .corner { position: absolute; top: 0; left: 0; }
  .card-back .brand-name {
    position: absolute;
    left: 0; right: 0; top: 140px;
    text-align: center;
    color: var(--paper);
    font-weight: 900;
    font-size: 104px;
    letter-spacing: 2px;
    line-height: 1;
  }
  /* front side */
  .logo-plate {
    position: absolute;
    top: 60px; left: 0;
    width: 210px; height: 58px;
    background: var(--paper);
    border-bottom: 8px solid var(--accent);
    display: flex; align-items: center; justify-content: center;
  }
  .logo-plate .brand-name {
    color: var(--ink);
    font-weight: 900;
    font-size: 32px;
    letter-spacing: 1px;
  }
  .person {
    position: absolute;
    top: 78px; left: 300px;
    color: var(--paper);
  }
  .person .name { font-size: 32px; font-weight: 400; line-height: 1.1; }
  .person .name strong { font-weight: 900; }
  .person .title {
    color: var(--accent);
    font-size: 12px; font-weight: 700;
    letter-spacing: 1.5px;
    text-transform: uppercase;
    margin-top: 3px;
  }
  .contacts {
    position: absolute;
    top: 148px; left: 300px;
    color: var(--paper);
    font-size: 18px;
    line-height: 24px;
    border-collapse: collapse;
  }
  .contacts th { text-align: left; font-weight: 700; padding: 0 10px 0 0; }
  .contacts td { font-weight: 400; padding: 0; }
  .address-band {
    position: absolute;
    left: 0; right: 0; bottom: 0;
    height: 50px;
    background: var(--accent);
    color: var(--paper);
    font-size: 17px; font-weight: 700;
    letter-spacing: 1px;
    display: flex; align-items: center;
    padding-left: 24px;
  }
</style>
</head>
<body>
  <section class="card card-back">
    <svg class="corner" width="90" height="50" viewBox="0 0 90 50" aria-hidden="true">
      <polygon points="0,0 90,0 0,50" fill="var(--accent)"/>
    </svg>
    <div class="brand-name">vextral</div>
  </section>

  <section class="card card-front">
    <div class="logo-plate"><span class="brand-name">vextral</span></div>
    <div class="person">
      <div class="name">Riley <strong>Tessmore</strong></div>
      <div class="title">Title goes here</div>
    </div>
    <table class="contacts">
      <tr><th>Cell</th><td>: +971 50 555 0100</td></tr>
      <tr><th>Phone</th><td>: 04 555 0100</td></tr>
      <tr><th>Fax</th><td>: 04 555 0101</td></tr>
      <tr><th>E-Mail</th><td>: name.surname@vextral.com</td></tr>
      <tr><th>Web</th><td>: www.vextral.com</td></tr>
    </table>
    <div class="address-band">Harbor Tech Park (HTP) -Coastal Ring Road. Marina - UAE</div>
  </section>
</body>
</html>
```